Apply Existing Website Design to Wexmoor-Made Tele-Wellness App (UX/UI Work)

We’re looking for a highly skilled UX/UI designer to translate our existing website design into an intuitive, beautiful mobile app interface for our Wexmoor-developed tele-wellness platform. Hoping this designer will stay onboard with us for future work.

Scope of Work:
    •    Review our existing website design (style, colors, typography, components)
    •    Apply the same visual language to our mobile app screens
    •    Ensure consistent, user-friendly experience across the app
    •    Deliver high-fidelity mockups and design assets (preferably in Figma)
    •    Minimal UX rethinking may be needed to optimize for mobile, but the core brand and design system are already established

What We Provide:
    •    Access to the existing website design (including any style guides or component libraries)
    •    Wireframes or a basic functional map of the app screens
    •    Clear guidelines on branding and user flows

Ideal Candidate:
    •    Strong portfolio of mobile app design, especially healthcare/wellness preferred
    •    Proven experience in adapting web designs for mobile apps
    •    Expertise with Figma or comparable tools
    •    Attention to detail and commitment to brand consistency
    •    Ability to deliver quickly while maintaining quality

Deliverables:
    •    Complete set of high-fidelity, mobile-optimized app screens
    •    Organized design file (Figma preferred) ready for developer handoff
    •    Design assets as needed (icons, images, components)

Timeline:
    •    Estimated 1 week for initial delivery, with room for revisions

```html
<!DOCTYPE html>
<html lang="en">
<head>
<meta charset="utf-8">
<title>Solvra Wellness App Screens</title>
<link href="https://fonts.googleapis.com/css2?family=Poppins:wght@300;400;500;600&display=swap" rel="stylesheet">
<style>
:root{
  --bg:#ebebeb;
  --ink:#1b1b1b;
  --muted:#8a8a8a;
  --body:#4a4a4a;
  --white:#ffffff;
  --black:#000000;
  --panel:#eeeeee;
  --peach:#ffc9a8;
  --peach-tile:#ffc0a0;
  --sky:#a9dcf3;
  --sky-tile:#a7dcf5;
  --lilac:#b48bf7;
  --lilac-tile:#b58cf5;
  --back-pill:#a8dcf5;
  --grad-start:#a62ef2;
  --grad-end:#6f86e6;
  --brand-gold:#f2c79b;
  --brand-soft:#b39a8c;
  --badge:#e5484d;
}
*{box-sizing:border-box;margin:0;padding:0}
html,body{width:1200px;height:1200px;overflow:hidden;background:var(--bg);font-family:'Poppins',sans-serif;color:var(--ink)}
.stage{position:absolute;left:0;top:0;width:1932px;height:1932px;transform:scale(0.62112);transform-origin:0 0}
.screen{position:absolute;width:290px;border-radius:18px;overflow:hidden;background:var(--white)}
.abs{position:absolute}

/* splash */
.splash{left:172px;top:476px;height:628px;background:var(--black)}
.splash .hero-art{left:52px;top:160px;width:186px;height:186px;border-radius:50%;background:radial-gradient(circle at 50% 45%,#b5444f 0%,#6b2426 55%,#3a1416 100%)}
.splash .brand{left:0;width:290px;top:372px;text-align:center;font-size:40px;font-weight:500;color:var(--brand-gold);letter-spacing:2px}
.splash .app-name{left:0;width:290px;top:426px;text-align:center;font-size:20px;font-weight:600;color:var(--brand-gold)}
.splash .tagline{left:0;width:290px;top:459px;text-align:center;font-size:14px;color:var(--brand-soft)}

/* intro */
.intro{left:501px;top:476px;height:628px;background:var(--black)}
.intro .photo{left:0;top:0;width:290px;height:504px;background:linear-gradient(180deg,#3f6b52 0%,#5b7d6f 35%,#8a9a98 60%,#2b3a3d 100%)}
.intro .pitch{left:10px;top:354px;width:270px;height:219px;border-radius:14px;background:linear-gradient(160deg,var(--grad-start) 0%,#8b4fee 50%,var(--grad-end) 100%);padding:30px 30px 0;color:var(--white)}
.pitch h2{font-size:16px;font-weight:400;line-height:23px}
.pitch p{font-size:11px;line-height:17px;margin-top:6px;font-weight:300}
.pitch p strong{font-weight:600}
.btn{display:inline-block;height:30px;line-height:30px;border-radius:6px;font-size:11px;font-weight:500;padding:0 12px}
.btn-solid{background:var(--white);color:var(--ink)}
.btn-ghost{border:1px solid var(--white);color:var(--white);line-height:28px}
.pitch .actions{margin-top:16px;display:flex;gap:7px}

/* app chrome */
.app{top:476px;height:829px}
.app.long{height:1041px}
.statusbar .time{left:28px;top:15px;font-size:13px;font-weight:600}
.statusbar .island{left:99px;top:10px;width:94px;height:26px;border-radius:13px;background:var(--black)}
.statusbar .icons{left:210px;top:17px}
.navbar{left:0;top:0;width:290px;height:92px;background:var(--white)}
.back-pill{left:17px;top:63px;height:16px;padding:0 7px;border-radius:8px;background:var(--back-pill);font-size:9px;line-height:16px}
.nav-title{left:0;width:290px;top:60px;text-align:center;font-size:14px}
.avatar{left:243px;top:55px;width:32px;height:32px;border-radius:50%;background:radial-gradient(circle,#8a5a48 0%,#c9a08e 100%)}
.content{left:0;top:92px;width:290px}
.page-title{left:9px;top:111px;font-size:16.5px;font-weight:400}
.page-sub{left:9px;top:140px;width:272px;font-size:9px;color:var(--body);line-height:14px;font-weight:300}
.tabbar{left:0;width:290px;height:68px;background:var(--white)}
.tabbar svg{position:absolute;top:16px}
.home-indicator{left:93px;width:104px;height:4px;border-radius:2px;background:var(--black)}

/* testimonials */
.quote{position:absolute;left:9px;width:270px;border-radius:10px;padding:12px 12px 0}
.quote h3{font-size:11px;font-weight:500;line-height:16px}
.quote p{font-size:8.6px;line-height:14px;color:var(--body);margin-top:6px}
.quote .author{display:flex;align-items:center;gap:9px;margin-top:8px;font-size:11px}
.author i{display:block;width:24px;height:24px;border-radius:50%;background:radial-gradient(circle,#6a4a3e 0%,#c7a996 100%)}
.q-peach{top:159px;height:165px;background:var(--peach)}
.q-sky{top:330px;height:164px;background:var(--sky)}
.q-lilac{top:501px;height:164px;background:var(--lilac)}
.stat-banner{left:9px;top:672px;width:270px;height:100px;border-radius:10px 10px 0 0;background:linear-gradient(100deg,#8a3cf0 0%,#6c7fe6 70%,#42b7c8 100%);padding:30px 31px 0;color:var(--white);font-size:16px;line-height:22px}

/* feature cards */
.feature{position:absolute;left:10px;width:270px;background:var(--white);border-radius:6px;text-align:center}
.tile{width:62px;height:62px;border-radius:10px;margin:18px auto 0;display:flex;align-items:center;justify-content:center}
.tile-peach{background:var(--peach-tile)}
.tile-sky{background:var(--sky-tile)}
.tile-lilac{background:var(--lilac-tile)}
.feature h4{font-size:11px;font-weight:500;line-height:16px;margin-top:18px;padding:0 20px}
.feature p{font-size:8.6px;line-height:14px;color:var(--muted);margin-top:14px;padding:0 18px}
.panel{background:var(--panel)}

.clarity{left:9px;top:192px;width:271px;height:175px;border-radius:10px;background:linear-gradient(150deg,var(--grad-start) 0%,#8b4fee 50%,var(--grad-end) 100%);padding:30px 31px 0;color:var(--white)}
.clarity h2{font-size:16px;font-weight:400;line-height:23.5px}
.clarity .btn{margin-top:18px}
</style>
</head>
<body>
<div class="stage">

  <!-- Splash -->
  <section class="screen splash">
    <div class="abs hero-art" role="img" aria-label="Illustration of a woman meditating in lotus pose inside a glowing red circle with birds"></div>
    <div class="abs brand">SOLVRA</div>
    <div class="abs app-name">Wellness App</div>
    <div class="abs tagline">Yoga &amp; Medititation</div>
  </section>

  <!-- Intro -->
  <section class="screen intro">
    <div class="abs photo" role="img" aria-label="Photo of a hooded figure with open arms in a misty forest"></div>
    <div class="abs pitch">
      <h2>Holistic-Doctor led care<br>Pay as you like</h2>
      <p>Evidence based care with heart<br>Tailored only for you Tele-Wellness<br><strong>Developed at Wexmoor</strong></p>
      <div class="actions"><span class="btn btn-solid">Book Now</span><span class="btn btn-ghost">Demo Video</span></div>
    </div>
  </section>

  <!-- Home: testimonials -->
  <section class="screen app" style="left:829px">
    <div class="abs navbar"></div>
    <div class="statusbar">
      <div class="abs time">9:41</div><div class="abs island"></div>
      <svg class="abs icons" width="64" height="12" viewBox="0 0 64 12"><rect x="0" y="8" width="2.5" height="3" fill="#000"/><rect x="4" y="6" width="2.5" height="5" fill="#000"/><rect x="8" y="4" width="2.5" height="7" fill="#000"/><rect x="12" y="1" width="2.5" height="10" fill="#000"/><path d="M20 4a9 9 0 0 1 12 0M22.5 6.5a5.5 5.5 0 0 1 7 0M26 10l-1.6-1.6a2.3 2.3 0 0 1 3.2 0z" stroke="#000" stroke-width="1.6" fill="none"/><rect x="38" y="1.5" width="19" height="9" rx="2.5" fill="#000"/><rect x="58" y="4.5" width="1.5" height="3" fill="#000"/></svg>
    </div>
    <div class="abs back-pill">Back</div>
    <div class="abs nav-title">Home</div>
    <div class="abs avatar" role="img" aria-label="User profile photo"></div>

    <div class="abs page-title">Trusted by: Northfield Apparel</div>
    <div class="abs page-sub">Pioneers in corporate wellness: A Better Way To Grow</div>

    <article class="quote q-peach">
      <h3>Chief Strategy Officer, National Tech Firm</h3>
      <p>For the first time in 20 years of nonstop output, I found a wellness system that didn’t just slow me down—it woke me up. Solvra’s personalized protocols gave me energy I didn’t know I was missing, and helped me show up sharper, calmer, and more focused than ever before.</p>
      <div class="author"><i role="img" aria-label="Reviewer photo"></i>David</div>
    </article>
    <article class="quote q-sky">
      <h3>Operations Supervisor,<br>Regional Distribution Center</h3>
      <p>Between shift work and stress, I was running on empty. Solvra didn’t hand me a generic plan-they listened. My sleep, digestion, and moods have all leveled out. I finally feel in control of my health, and my team noticed the difference too.</p>
      <div class="author"><i role="img" aria-label="Reviewer photo"></i>Joshua</div>
    </article>
    <article class="quote q-lilac">
      <h3>Warehouse Associate,<br>National Retail Chain</h3>
      <p>I never thought wellness was made for someone like me. Solvra changed that. They spoke my language, respected my time, and helped my body stop hurting every day. It’s not just medicine-it’s care that fits real life</p>
      <div class="author"><i role="img" aria-label="Reviewer photo"></i>Joshua</div>
    </article>
    <div class="abs stat-banner">55 Million Bio-Markers<br>analysed</div>

    <div class="abs tabbar" style="top:761px">
      <svg style="left:28px" width="18" height="18" viewBox="0 0 18 18"><rect x="2" y="3" width="14" height="13" rx="2.5" fill="#111"/><rect x="5" y="1" width="1.6" height="4" fill="#111"/><rect x="11.4" y="1" width="1.6" height="4" fill="#111"/><rect x="5" y="9" width="2" height="2" fill="#fff"/></svg>
      <svg style="left:99px" width="20" height="20" viewBox="0 0 20 20"><circle cx="9" cy="9" r="7" stroke="#aaa" stroke-width="1.3" fill="none"/><path d="M14 14l4 4" stroke="#aaa" stroke-width="1.3"/></svg>
      <svg style="left:170px;top:10px" width="40" height="26" viewBox="0 0 40 26"><rect x="2" y="8" width="15" height="14" rx="3" stroke="#aaa" stroke-width="1.3" fill="none"/><path d="M6 14h7M6 17h5" stroke="#aaa" stroke-width="1.2"/><rect x="14" y="1" width="22" height="11" rx="5.5" fill="#e5484d"/><text x="25" y="9.5" font-size="7.5" fill="#fff" text-anchor="middle" font-family="Poppins,sans-serif">99+</text></svg>
      <svg style="left:244px" width="16" height="16" viewBox="0 0 16 16"><circle cx="3" cy="3" r="2" stroke="#aaa" fill="none"/><circle cx="13" cy="3" r="2" stroke="#aaa" fill="none"/><circle cx="3" cy="13" r="2" stroke="#aaa" fill="none"/><circle cx="13" cy="13" r="2" stroke="#aaa" fill="none"/></svg>
    </div>
    <div class="abs home-indicator" style="top:820px"></div>
  </section>

  <!-- Home: difference -->
  <section class="screen app panel" style="left:1150px">
    <div class="abs navbar"></div>
    <div class="statusbar">
      <div class="abs time">9:41</div><div class="abs island"></div>
      <svg class="abs icons" width="64" height="12" viewBox="0 0 64 12"><rect x="0" y="8" width="2.5" height="3" fill="#000"/><rect x="4" y="6" width="2.5" height="5" fill="#000"/><rect x="8" y="4" width="2.5" height="7" fill="#000"/><rect x="12" y="1" width="2.5" height="10" fill="#000"/><path d="M20 4a9 9 0 0 1 12 0M22.5 6.5a5.5 5.5 0 0 1 7 0M26 10l-1.6-1.6a2.3 2.3 0 0 1 3.2 0z" stroke="#000" stroke-width="1.6" fill="none"/><rect x="38" y="1.5" width="19" height="9" rx="2.5" fill="#000"/><rect x="58" y="4.5" width="1.5" height="3" fill="#000"/></svg>
    </div>
    <div class="abs back-pill">Back</div>
    <div class="abs nav-title">Home</div>
    <div class="abs avatar" role="img" aria-label="User profile photo"></div>

    <div class="abs page-title">The Solvra Difference</div>
    <div class="abs page-sub">Pioneers in corporate wellness: A Better Way To Grow</div>

    <div class="feature" style="top:173px;height:168px">
      <div class="tile tile-peach"><svg width="30" height="30" viewBox="0 0 30 30"><circle cx="15" cy="15" r="9" stroke="#fff" stroke-width="1.4" fill="none"/><path d="M10.5 15.5l3 3 6-6" stroke="#fff" stroke-width="1.4" fill="none"/></svg></div>
      <h4>Precision You Can Trust</h4>
      <p>Doctors cross- trained in time tested<br>and modern science</p>
    </div>
    <div class="feature" style="top:350px;height:168px">
      <div class="tile tile-sky"><svg width="30" height="30" viewBox="0 0 30 30"><circle cx="15" cy="15" r="9" stroke="#fff" stroke-width="1.4" fill="none"/><path d="M10.5 15.5l3 3 6-6" stroke="#fff" stroke-width="1.4" fill="none"/></svg></div>
      <h4>Care You Can Feel</h4>
      <p>Plans crafted around your<br>whole self &amp; labs</p>
    </div>
    <div class="feature" style="top:527px;height:167px">
      <div class="tile tile-lilac"><svg width="30" height="30" viewBox="0 0 30 30"><circle cx="15" cy="15" r="9" stroke="#fff" stroke-width="1.4" fill="none"/><path d="M10.5 15.5l3 3 6-6" stroke="#fff" stroke-width="1.4" fill="none"/></svg></div>
      <h4>Ethics You Can Stand Behind</h4>
      <p>Fair-trade sourcing,<br>real transparency</p>
    </div>

    <div class="abs tabbar" style="top:761px">
      <svg style="left:28px" width="18" height="18" viewBox="0 0 18 18"><rect x="2" y="3" width="14" height="13" rx="2.5" fill="#111"/><rect x="5" y="1" width="1.6" height="4" fill="#111"/><rect x="11.4" y="1" width="1.6" height="4" fill="#111"/><rect x="5" y="9" width="2" height="2" fill="#fff"/></svg>
      <svg style="left:99px" width="20" height="20" viewBox="0 0 20 20"><circle cx="9" cy="9" r="7" stroke="#aaa" stroke-width="1.3" fill="none"/><path d="M14 14l4 4" stroke="#aaa" stroke-width="1.3"/></svg>
      <svg style="left:170px;top:10px" width="40" height="26" viewBox="0 0 40 26"><rect x="2" y="8" width="15" height="14" rx="3" stroke="#aaa" stroke-width="1.3" fill="none"/><path d="M6 14h7M6 17h5" stroke="#aaa" stroke-width="1.2"/><rect x="14" y="1" width="22" height="11" rx="5.5" fill="#e5484d"/><text x="25" y="9.5" font-size="7.5" fill="#fff" text-anchor="middle" font-family="Poppins,sans-serif">99+</text></svg>
      <svg style="left:244px" width="16" height="16" viewBox="0 0 16 16"><circle cx="3" cy="3" r="2" stroke="#aaa" fill="none"/><circle cx="13" cy="3" r="2" stroke="#aaa" fill="none"/><circle cx="3" cy="13" r="2" stroke="#aaa" fill="none"/><circle cx="13" cy="13" r="2" stroke="#aaa" fill="none"/></svg>
    </div>
    <div class="abs home-indicator" style="top:820px"></div>
  </section>

  <!-- Home: results -->
  <section class="screen app long panel" style="left:1471px">
    <div class="abs navbar"></div>
    <div class="statusbar">
      <div class="abs time">9:41</div><div class="abs island"></div>
      <svg class="abs icons" width="64" height="12" viewBox="0 0 64 12"><rect x="0" y="8" width="2.5" height="3" fill="#000"/><rect x="4" y="6" width="2.5" height="5" fill="#000"/><rect x="8" y="4" width="2.5" height="7" fill="#000"/><rect x="12" y="1" width="2.5" height="10" fill="#000"/><path d="M20 4a9 9 0 0 1 12 0M22.5 6.5a5.5 5.5 0 0 1 7 0M26 10l-1.6-1.6a2.3 2.3 0 0 1 3.2 0z" stroke="#000" stroke-width="1.6" fill="none"/><rect x="38" y="1.5" width="19" height="9" rx="2.5" fill="#000"/><rect x="58" y="4.5" width="1.5" height="3" fill="#000"/></svg>
    </div>
    <div class="abs back-pill">Back</div>
    <div class="abs nav-title">Home</div>
    <div class="abs avatar" role="img" aria-label="User profile photo"></div>

    <div class="abs page-title">Time Tested and Results Driven</div>
    <div class="abs page-sub">We get it. You’ve tried the threads, the threads on the threads. It’s time for something real-and built around you, clarity is a form of care.</div>

    <div class="abs clarity">
      <h2>Three minutes.<br>No commitment.<br>Much clarity.</h2>
      <span class="btn btn-solid">Book Now</span>
    </div>

    <div class="feature" style="top:384px;height:210px">
      <div class="tile tile-peach"><svg width="30" height="30" viewBox="0 0 30 30"><circle cx="15" cy="15" r="9" stroke="#fff" stroke-width="1.4" fill="none"/><path d="M10.5 15.5l3 3 6-6" stroke="#fff" stroke-width="1.4" fill="none"/></svg></div>
      <h4>Conflicted by fad-driven advice and endless tests without real insight?</h4>
      <p>Solvra cuts through the noise with time-tested, evidence-based care and real credentials-thousands of years of wisdom versus a few years of fragmented information in holistic medicine.</p>
    </div>
    <div class="feature" style="top:603px;height:236px">
      <div class="tile tile-sky"><svg width="30" height="30" viewBox="0 0 30 30"><circle cx="15" cy="15" r="9" stroke="#fff" stroke-width="1.4" fill="none"/><path d="M10.5 15.5l3 3 6-6" stroke="#fff" stroke-width="1.4" fill="none"/></svg></div>
      <h4>Tired of one-size-fits-all supplements?</h4>
      <p>At Solvra, every formula is tailored to your unique mind-body type. No algorithms. No shortcuts. Just real doctors creating real, time-tested protocols-just for you. We don’t do “standard.” Solvra formulas are hand-built by doctors to reflect your specific constitution, habits, and environment. You deserve precision-not guesswork.</p>
    </div>
    <div class="feature" style="top:848px;height:140px">
      <div class="tile tile-sky"><svg width="30" height="30" viewBox="0 0 30 30"><circle cx="15" cy="15" r="9" stroke="#fff" stroke-width="1.4" fill="none"/><path d="M10.5 15.5l3 3 6-6" stroke="#fff" stroke-width="1.4" fill="none"/></svg></div>
      <h4>Being overcharged by underqualified, self-professed experts?</h4>
    </div>

    <div class="abs tabbar" style="top:974px">
      <svg style="left:28px" width="18" height="18" viewBox="0 0 18 18"><rect x="2" y="3" width="14" height="13" rx="2.5" fill="#111"/><rect x="5" y="1" width="1.6" height="4" fill="#111"/><rect x="11.4" y="1" width="1.6" height="4" fill="#111"/><rect x="5" y="9" width="2" height="2" fill="#fff"/></svg>
      <svg style="left:99px" width="20" height="20" viewBox="0 0 20 20"><circle cx="9" cy="9" r="7" stroke="#aaa" stroke-width="1.3" fill="none"/><path d="M14 14l4 4" stroke="#aaa" stroke-width="1.3"/></svg>
      <svg style="left:170px;top:10px" width="40" height="26" viewBox="0 0 40 26"><rect x="2" y="8" width="15" height="14" rx="3" stroke="#aaa" stroke-width="1.3" fill="none"/><path d="M6 14h7M6 17h5" stroke="#aaa" stroke-width="1.2"/><rect x="14" y="1" width="22" height="11" rx="5.5" fill="#e5484d"/><text x="25" y="9.5" font-size="7.5" fill="#fff" text-anchor="middle" font-family="Poppins,sans-serif">99+</text></svg>
      <svg style="left:244px" width="16" height="16" viewBox="0 0 16 16"><circle cx="3" cy="3" r="2" stroke="#aaa" fill="none"/><circle cx="13" cy="3" r="2" stroke="#aaa" fill="none"/><circle cx="3" cy="13" r="2" stroke="#aaa" fill="none"/><circle cx="13" cy="13" r="2" stroke="#aaa" fill="none"/></svg>
    </div>
    <div class="abs home-indicator" style="top:1032px"></div>
  </section>

</div>
</body>
</html>
```